Vantor - Transport company looking for a basic but smart design for the sides of our trailers

We have a logo 'Vantor' which i would like to keep.
We have 2 companies Vantor Haulage - Maroon signwriting (general freight ) and Vantor Refrigerated - Blue signwriting (refrigerated freight) that can share the same design.
I'd like to come up with a basic modern design that will incorporate the Vantor logo, the company name and the website and maybe an image at the front od some sort, a 3D swish or a stripe or something.
The Vantor Haulage maroon trailers are too busy and I don't like the icicles on the front of the Vantor Refrigerated blue trailers.

```html
<!DOCTYPE html>
<html lang="en">
<head>
<meta charset="utf-8">
<title>Vantor Trailer Side Designs</title>
<link href="https://fonts.googleapis.com/css2?family=Roboto+Condensed:wght@700&family=Arimo:wght@400&display=swap" rel="stylesheet">
<style>
  :root{
    --stage:#000000;
    --paper:#ffffff;
    --maroon:#7d0c05;
    --ink:#3a3a3a;
    --web-ink:#333333;
    --warm-deep:#8a1010;
    --warm-mid:#f0801f;
    --warm-light:#ffff40;
    --cool-deep:#262660;
    --cool-mid:#1f7fcc;
    --cool-light:#40c0f0;
  }
  html,body{margin:0;padding:0;overflow:hidden;}
  body{width:1200px;height:1200px;background:var(--stage);position:relative;}
  .trailer-panel{position:absolute;left:129px;width:940px;height:283px;display:block;}
  .trailer-panel--haulage{top:106px;}
  .trailer-panel--refrigerated{top:496px;}
  .panel-base{fill:var(--paper);}
  .brand-name{fill:var(--maroon);font-family:"Roboto Condensed",sans-serif;font-weight:700;font-size:120px;}
  .web-address{fill:var(--web-ink);font-family:"Arimo",sans-serif;font-size:34px;}
  .company-line{fill:var(--ink);font-family:"Roboto Condensed",sans-serif;font-weight:700;font-size:32px;}
</style>
</head>
<body>

<!-- Haulage (warm) trailer side -->
<svg class="trailer-panel trailer-panel--haulage" viewBox="0 0 1514 455" preserveAspectRatio="none">
  <defs>
    <linearGradient id="haulage-wash" x1="0" y1="0" x2="1" y2="0">
      <stop offset="0" stop-color="var(--warm-deep)"/>
      <stop offset=".12" stop-color="#e8323a"/>
      <stop offset=".24" stop-color="var(--warm-mid)"/>
      <stop offset=".33" stop-color="var(--warm-light)"/>
      <stop offset=".38" stop-color="var(--paper)"/>
      <stop offset=".67" stop-color="var(--paper)"/>
      <stop offset=".74" stop-color="var(--warm-light)"/>
      <stop offset=".84" stop-color="var(--warm-mid)"/>
      <stop offset=".92" stop-color="#e8323a"/>
      <stop offset="1" stop-color="var(--warm-deep)"/>
    </linearGradient>
  </defs>
  <rect class="panel-base" width="1514" height="455"/>
  <rect width="1514" height="455" fill="url(#haulage-wash)" role="img" aria-label="Warm red to yellow swoosh artwork with stars on both ends of the trailer"/>
  <text class="web-address" x="340" y="62" textLength="672" lengthAdjust="spacing">www.vantorhaulage.com</text>
  <text class="brand-name" x="797" y="268" text-anchor="middle">VANTOR</text>
  <text class="company-line" x="860" y="378" text-anchor="middle">VANTOR HAULAGE</text>
  <text class="company-line" x="860" y="414" text-anchor="middle">VANTOR REFRIGERATED</text>
</svg>

<!-- Refrigerated (cool) trailer side -->
<svg class="trailer-panel trailer-panel--refrigerated" viewBox="0 0 1514 455" preserveAspectRatio="none">
  <defs>
    <linearGradient id="refrigerated-wash" x1="0" y1="0" x2="1" y2="0">
      <stop offset="0" stop-color="var(--cool-deep)"/>
      <stop offset=".12" stop-color="#3d3d96"/>
      <stop offset=".24" stop-color="var(--cool-mid)"/>
      <stop offset=".33" stop-color="var(--cool-light)"/>
      <stop offset=".38" stop-color="var(--paper)"/>
      <stop offset=".67" stop-color="var(--paper)"/>
      <stop offset=".74" stop-color="var(--cool-light)"/>
      <stop offset=".84" stop-color="var(--cool-mid)"/>
      <stop offset=".92" stop-color="#3d3d96"/>
      <stop offset="1" stop-color="var(--cool-deep)"/>
    </linearGradient>
  </defs>
  <rect class="panel-base" width="1514" height="455"/>
  <rect width="1514" height="455" fill="url(#refrigerated-wash)" role="img" aria-label="Cool navy to sky blue swoosh artwork with stars on both ends of the trailer"/>
  <text class="web-address" x="340" y="62" textLength="672" lengthAdjust="spacing">www.vantorhaulage.com</text>
  <text class="brand-name" x="797" y="268" text-anchor="middle">VANTOR</text>
  <text class="company-line" x="860" y="378" text-anchor="middle">VANTOR HAULAGE</text>
  <text class="company-line" x="860" y="414" text-anchor="middle">VANTOR REFRIGERATED</text>
</svg>
</body>
</html>
```